Brochure Design Project for Family and Cosmetic Dental Practice

Family and Cosmetic Dental Practice with Ocean/Tropical Theme
Here is some more information about my business. We also have a website :www.marbrookfamilydentistry.com. That has a video that we made and gives you a some more information about us.

An Overview / Background of the Business & Services :

Family and Cosmetic Dental Practice

Procedures that we do:

Clarotrack (Clear Braces)

Dentures and Partials

Whitening/ Teeth Bleaching (both Pell and Vix)

Cosmetic Dentistry (veneers and esthetic crowns)

Implants

Children's Dentistry

Sedation Dentistry and Nitrous Oxide Gas (Laughing Gas)

The Target Market / Audience you are trying to reach:

Families (30 to 40 yrs with children) - Caucasians and Hispanics
People seeking cosmetic dentistry
Older Patients (50yrs +)

Design Specifics; any preferences or ideas for Style, Colour, Imagery, etc :

Color: Blues

Theme: Ocean/ Tropical

Our Philosophy

Our belief is that the best oral care that you receive is at home where you are able to maintain your oral hygiene through proper brushing, flossing and control of your diet. We would like to see you maintain your natural teeth for the rest of your life. When this is not possible we will work with you to replace them with the best aesthetic and functional restorative dentistry
that is available.

We want to let people we have been at our location for 10 years and we are family owned and are here for the long run. We are active in the community

Bios of the doctors: ( I already sent the headshot photos)

Dr Martin Keswick
“Dr. Marty”

Dr. Marty Keswick attended Fenwood University for his undergraduate studies and earned a Bachelor’s degree in Chemistry. While attending Fenwood he pursued his passion of running and was a member of two Midplains League Champion cross country teams. His passion for running evolved into a desire to compete in triathlons. He continued his interest in the sciences and working with his hands by attending the Drummond State College School of Dentistry where he met his wife, Clare Keswick D.D.S. and earned his D.D.S. with honors in Oral Surgery. He has practiced the last few years in Tucson treating a wide range of patients. His desire to practice dentistry revolves around the patient and service. Some of his hobby highlights include finishing the Desert Steelrace triathlon in 11 hours and 37 minutes in 2005 and a single digit golf handicap. His current passion is mountain biking. He recently finished the Pinecrest Trail Cycling race (100 miles in one day)! Lately he spends a lot of time caring for and playing with his 3 daughters. Dr. Marty Keswick is also a member of NOH (National Oral Health Union), SwOG (Southwest Oral Guild) and CFP (College of Family Practitioners).

Dr. Clare Keswick
“Dr. Keswick”

Dr. Clare Keswick attended both Harrowgate University and Northern Crestfield University for her undergraduate degrees. She received a Bachelor of Science in Biology and a Bachelor of Arts in Psychology. After college, Dr Keswick worked for several years in the dental field while continuing her education by working towards a Master’s degree in Cell and Molecular Biology. At this point in her life Dr. Keswick knew that she enjoyed the dental field and decided to attend dental school. Dr. Keswick completed her Doctorate of Dental Surgery (D.D.S.) at Drummond State College where she met her husband, Dr. Martin Keswick. They then moved to Tucson, Arizona in order to be close to family. When Dr. Clare isn't in the office creating beautiful smiles, she is busy with her 3 daughters and their numerous activities. Dr. Clare Keswick has additional training in the areas of endodontics and oral sedation. She is also a member of The National College of Family Practitioners (NCFP), National Oral Health Union (NOH), and Southwest Oral Guild (SwOG). In her time outside of the office, Dr. Keswick enjoys traveling, spending time with her family, working out and being involved with book club.
Let me know if you need anything else!

Target Market(s)

See above

Industry/Entity Type

Business

Colors
33a6d7
85cae6
33b8a4

Requirements
Must have
• Testimonials taken from Reviewly reviews. In any images used, the people must have nice smiles and teeth.

```html
<!DOCTYPE html>
<html lang="en">
<head>
<meta charset="utf-8">
<title>Marbrook Family Dentistry – Tri-fold Brochure</title>
<link rel="stylesheet" href="https://fonts.googleapis.com/css2?family=Source+Sans+3:ital,wght@0,300;0,400;0,600;0,700;1,400&family=Arimo:wght@400&family=Crimson+Text&display=swap">
<style>
  :root {
    --backdrop: #2e2e2e;
    --brand-blue: #33a6d7;
    --brand-sky: #85cae6;
    --brand-teal: #33b8a4;
    --deep-blue: #1d8fcf;
    --ink: #222;
    --ink-soft: #3a3a3a;
    --white: #fff;
    --check: #3aa0d8;
    --rule: #9aa3a8;
  }
  * { box-sizing: border-box; margin: 0; padding: 0; }
  html, body { width: 891px; height: 1200px; overflow: hidden; }
  body { background: var(--backdrop); font-family: "Source Sans 3", Arial, sans-serif; color: var(--ink); position: relative; }

  .sheet { position: absolute; left: 84px; width: 725px; height: 560px; overflow: hidden; }
  .sheet--outside { top: 25px; }
  .sheet--inside { top: 616px; }
  .sheet__art { position: absolute; inset: 0; }

  /* Outside */
  .philosophy { position: absolute; left: 15px; top: 223px; width: 218px; color: var(--white); }
  .philosophy__title { font-weight: 300; font-size: 29px; line-height: 35px; letter-spacing: .3px; }
  .philosophy__body { margin-top: 9px; font-family: "Arimo", Arial, sans-serif; font-size: 8.9px; line-height: 14.7px; }
  .philosophy__body p + p { margin-top: 14.7px; }

  .contact-intro { position: absolute; left: 250px; top: 72px; width: 225px; text-align: center; font-style: italic; font-size: 11.5px; line-height: 16.5px; color: var(--ink-soft); }
  .contact { position: absolute; left: 250px; top: 428px; width: 225px; text-align: center; color: var(--white); }
  .contact__address { font-size: 12.4px; line-height: 18px; }
  .contact__phone { margin-top: 8px; font-size: 21px; font-weight: 700; letter-spacing: .3px; }
  .contact__web { margin-top: 7px; font-size: 12.4px; }

  .brand { position: absolute; left: 503px; top: 30px; width: 200px; }
  .brand__row { display: flex; align-items: center; gap: 8px; }
  .brand__mark { width: 60px; height: 60px; border: 2px solid var(--ink); flex: none; }
  .brand__name { font-size: 18px; line-height: 21px; letter-spacing: 3px; color: var(--ink); font-weight: 400; }
  .brand__since { margin-top: 8px; text-align: center; font-size: 9.5px; letter-spacing: 1.4px; color: var(--ink-soft); padding-left: 30px; }

  .tagline { position: absolute; left: 490px; top: 422px; width: 228px; text-align: center; font-family: "Crimson Text", Georgia, serif; font-size: 22.5px; line-height: 29px; color: var(--ink); }
  .tagline-web { position: absolute; left: 490px; top: 504px; width: 228px; text-align: center; font-size: 12.4px; color: var(--ink); }

  /* Inside */
  .section-title { position: absolute; font-weight: 300; font-size: 26px; color: var(--ink); letter-spacing: .3px; }
  .section-title--doctors { left: 250px; width: 224px; top: 10px; text-align: center; }
  .section-title--services { left: 16px; top: 206px; }
  .section-title--testimonials { left: 494px; top: 253px; }

  .services { position: absolute; left: 16px; top: 247px; list-style: none; font-family: "Arimo", Arial, sans-serif; font-size: 9.8px; color: var(--ink-soft); }
  .services li { position: relative; padding-left: 19px; min-height: 22px; line-height: 13px; }
  .services li svg { position: absolute; left: 0; top: 1px; }
  .services .services__sub { display: block; padding-left: 12px; margin-top: 3px; }

  .doctor__name { position: absolute; left: 344px; font-size: 11.5px; font-weight: 700; color: var(--ink); }
  .doctor__bio { position: absolute; left: 250px; width: 224px; font-size: 7px; line-height: 9.9px; text-align: justify; color: var(--ink-soft); }
  .doctor__bio::before { content: ""; float: left; width: 94px; height: 59px; }
  .doctor--martin .doctor__name { top: 60px; }
  .doctor--martin .doctor__bio { top: 84px; }
  .doctor--clare .doctor__name { top: 312px; }
  .doctor--clare .doctor__bio { top: 336px; }
  .doctor-divider { position: absolute; left: 250px; top: 294px; width: 224px; height: 1px; background: var(--rule); }

  .testimonials { position: absolute; left: 524px; top: 302px; width: 186px; display: flex; flex-direction: column; }
  .testimonial { font-style: italic; font-size: 9.6px; line-height: 14.8px; color: var(--ink-soft); }
  .testimonial-divider { width: 204px; height: 1px; margin: 7px 0 8px -20px; background: var(--rule); }
  .quote-mark { position: absolute; font-family: Georgia, serif; font-size: 58px; line-height: 1; color: #b9c2c6; font-weight: 700; }
  .quote-mark--open { left: 494px; top: 290px; }
  .quote-mark--close { left: 690px; top: 514px; }
</style>
</head>
<body>

<section class="sheet sheet--outside">
  <svg class="sheet__art" width="725" height="560" viewBox="0 0 725 560">
    <defs>
      <linearGradient id="sea" x1="0" y1="0" x2="0" y2="1">
        <stop offset="0" stop-color="#cfe6f3"/>
        <stop offset=".28" stop-color="#a7d4ea"/>
        <stop offset=".42" stop-color="#4fa6cf"/>
        <stop offset=".7" stop-color="#8fc9e2"/>
        <stop offset="1" stop-color="#d9eef5"/>
      </linearGradient>
      <linearGradient id="sand" x1="0" y1="0" x2="0" y2="1">
        <stop offset="0" stop-color="#e3ddd2"/>
        <stop offset="1" stop-color="#d8cbb6"/>
      </linearGradient>
      <linearGradient id="panelBlue" x1="0" y1="0" x2="1" y2="1">
        <stop offset="0" stop-color="#2ba3dd"/>
        <stop offset="1" stop-color="#1c8fd0"/>
      </linearGradient>
    </defs>
    <rect width="725" height="560" fill="url(#sea)"/>
    <rect x="483" y="290" width="242" height="270" fill="url(#sand)"/>
    <rect x="483" y="170" width="242" height="200" fill="#d9c9bd" opacity=".75" role="img" aria-label="Photo of a smiling family of four on the beach"/>
    <rect x="0" y="0" width="241" height="262" fill="#7a6f68" role="img" aria-label="Photo of the two dentists standing in the office reception"/>
    <path d="M0,124 C70,170 160,220 241,236 L241,560 L0,560 Z" fill="#fff" opacity=".85"/>
    <path d="M0,132 C70,180 160,230 241,248 C300,262 380,300 483,340 L483,560 L0,560 Z" fill="url(#panelBlue)"/>
    <path d="M241,248 C300,262 380,300 483,340" fill="none" stroke="#fff" stroke-width="5" opacity=".7"/>
    <circle cx="362" cy="296" r="98" fill="#fff"/>
    <circle cx="362" cy="296" r="92" fill="#e6e1d6" role="img" aria-label="Street map showing the office location"/>
    <path d="M362,296 l-8,-12 h16 z" fill="#4caf50" stroke="#2e7d32"/>
  </svg>

  <div class="philosophy">
    <h2 class="philosophy__title">OUR<br>PHILOSOPHY</h2>
    <div class="philosophy__body">
      <p>Our belief is that the best oral care that you receive is at home where you are able to maintain your oral hygiene through proper brushing, flossing and control of your diet. We would like to see you maintain your natural teeth for the rest of your life. When this is not possible we will work with you to replace them with the best aesthetic and functional restorative dentistry that is available.</p>
      <p>We will help to educate you on what is occurring in your mouth and will discuss how to maintain good oral hygiene or what is needed in order to get your mouth back to a healthy state. We encourage you to ask questions about the treatment that you need so that you will have a good understanding of your oral health.</p>
    </div>
  </div>

  <p class="contact-intro">We encourage you to contact us<br>with any questions or comments<br>you may have</p>

  <div class="contact">
    <p class="contact__address">4120 East Harbor Crest Road<br>Suite 210, Larkfield, AZ 85006</p>
    <p class="contact__phone">480-555-0147</p>
    <p class="contact__web">www.marbrookfamilydentistry.com</p>
  </div>

  <div class="brand">
    <div class="brand__row">
      <span class="brand__mark"></span>
      <span class="brand__name">MARBROOK<br>FAMILY<br>DENTISTRY</span>
    </div>
    <p class="brand__since">Established in 2006</p>
  </div>

  <p class="tagline">Quality Dentistry With<br>a Compassionate Touch</p>
  <p class="tagline-web">www.marbrookfamilydentistry.com</p>
</section>

<section class="sheet sheet--inside">
  <svg class="sheet__art" width="725" height="560" viewBox="0 0 725 560">
    <defs>
      <linearGradient id="beach" x1="0" y1="0" x2="0" y2="1">
        <stop offset="0" stop-color="#eef5f8"/>
        <stop offset=".3" stop-color="#d5e9f2"/>
        <stop offset=".55" stop-color="#a9d4e8"/>
        <stop offset=".75" stop-color="#dbeef4"/>
        <stop offset="1" stop-color="#f1eee8"/>
      </linearGradient>
    </defs>
    <rect width="725" height="560" fill="url(#beach)"/>
    <circle cx="120" cy="100" r="92" fill="#fff" opacity=".9"/>
    <circle cx="120" cy="100" r="86" fill="#c9cdd0" role="img" aria-label="Photo of dental instruments"/>
    <circle cx="296" cy="92" r="40" fill="#fff"/>
    <circle cx="296" cy="92" r="37" fill="#c7b5a6" role="img" aria-label="Headshot of Dr. Martin Keswick"/>
    <circle cx="296" cy="344" r="40" fill="#fff"/>
    <circle cx="296" cy="344" r="37" fill="#d1bfa9" role="img" aria-label="Headshot of Dr. Clare Keswick"/>
    <circle cx="616" cy="110" r="98" fill="#fff" opacity=".9"/>
    <circle cx="616" cy="110" r="92" fill="#b9a08e" role="img" aria-label="Photo of a smiling young man"/>
    <circle cx="556" cy="186" r="57" fill="#fff"/>
    <circle cx="556" cy="186" r="52" fill="#9c8376" role="img" aria-label="Photo of a smiling woman"/>
  </svg>

  <h2 class="section-title section-title--doctors">OUR DOCTORS</h2>

  <article class="doctor doctor--martin">
    <h3 class="doctor__name">Dr Martin Keswick</h3>
    <p class="doctor__bio">Dr. Marty Keswick attended Fenwood University for his undergraduate studies and earned a Bachelor’s degree in Chemistry. While attending Fenwood he pursued his passion of running and was a member of two Midplains League Champion cross country teams. His passion for running evolved into a desire to compete in triathlons. He continued his interest in the sciences and working with his hands by attending the Drummond State College School of Dentistry where he met his wife, Clare Keswick D.D.S. He practiced for 3 years in Tucson treating a wide range of patients. His desire to practice dentistry revolves around the patient and service. Some of his hobby highlights include finishing the Desert Steelrace triathlon in 11 hours and 37 minutes in 2005 and a single digit golf handicap. His current passion is mountain biking. He recently finished the Pinecrest Trail Cycling race (100 miles in one day)! Lately he spends a lot of time caring for and playing with his 3 daughters. Dr. Marty Keswick is also a member of NOH (National Oral Health Union), SwOG (Southwest Oral Guild) and CFP (College of Family Practitioners).</p>
  </article>

  <div class="doctor-divider"></div>

  <article class="doctor doctor--clare">
    <h3 class="doctor__name">Dr. Clare Keswick</h3>
    <p class="doctor__bio">Dr. Clare Keswick attended both Harrowgate University and Northern Crestfield University for her undergraduate degrees. She received a Bachelor of Science in Biology and a Bachelor of Arts in Psychology. After college, Dr Keswick worked for several years in the dental field while continuing her education by working towards a Master’s degree in Cell and Molecular Biology. At this point in her life Dr. Keswick knew that she enjoyed the dental field and decided to attend dental school. Dr. Keswick completed her Doctorate of Dental Surgery (D.D.S.) at Drummond State College where she met her husband, Dr. Martin Keswick. They then moved to Tucson, Arizona in order to be close to family. When Dr. Clare isn't in the office creating beautiful smiles, she is busy with her 3 daughters and their numerous activities. She is a member of The National College of Family Practitioners (NCFP), National Oral Health Union (NOH), and Southwest Oral Guild (SwOG). Currently, Dr. Clare Keswick is working towards accreditation with the National Guild of Cosmetic Practice. In her time outside of the office, Dr. Keswick enjoys traveling, spending time with her family, working out and being involved with book club.</p>
  </article>

  <h2 class="section-title section-title--services">SERVICES</h2>
  <ul class="services">
    <li><svg width="11" height="11" viewBox="0 0 11 11"><circle cx="5.5" cy="5.5" r="4.6" fill="none" stroke="var(--check)" stroke-width="1.2"/><path d="M3,5.6 L5,7.4 L9.6,2.4" fill="none" stroke="var(--check)" stroke-width="1.4"/></svg>Teeth Cleaning</li>
    <li><svg width="11" height="11" viewBox="0 0 11 11"><circle cx="5.5" cy="5.5" r="4.6" fill="none" stroke="var(--check)" stroke-width="1.2"/><path d="M3,5.6 L5,7.4 L9.6,2.4" fill="none" stroke="var(--check)" stroke-width="1.4"/></svg>Cosmetic Dentistry</li>
    <li><svg width="11" height="11" viewBox="0 0 11 11"><circle cx="5.5" cy="5.5" r="4.6" fill="none" stroke="var(--check)" stroke-width="1.2"/><path d="M3,5.6 L5,7.4 L9.6,2.4" fill="none" stroke="var(--check)" stroke-width="1.4"/></svg>Composite (White) Fillings</li>
    <li><svg width="11" height="11" viewBox="0 0 11 11"><circle cx="5.5" cy="5.5" r="4.6" fill="none" stroke="var(--check)" stroke-width="1.2"/><path d="M3,5.6 L5,7.4 L9.6,2.4" fill="none" stroke="var(--check)" stroke-width="1.4"/></svg>Porcelain Crowns (Caps)</li>
    <li><svg width="11" height="11" viewBox="0 0 11 11"><circle cx="5.5" cy="5.5" r="4.6" fill="none" stroke="var(--check)" stroke-width="1.2"/><path d="M3,5.6 L5,7.4 L9.6,2.4" fill="none" stroke="var(--check)" stroke-width="1.4"/></svg>Dental Implants</li>
    <li><svg width="11" height="11" viewBox="0 0 11 11"><circle cx="5.5" cy="5.5" r="4.6" fill="none" stroke="var(--check)" stroke-width="1.2"/><path d="M3,5.6 L5,7.4 L9.6,2.4" fill="none" stroke="var(--check)" stroke-width="1.4"/></svg>Veneers</li>
    <li style="min-height:38px"><svg width="11" height="11" viewBox="0 0 11 11"><circle cx="5.5" cy="5.5" r="4.6" fill="none" stroke="var(--check)" stroke-width="1.2"/><path d="M3,5.6 L5,7.4 L9.6,2.4" fill="none" stroke="var(--check)" stroke-width="1.4"/></svg>Teeth Whitening<span class="services__sub">- Pell and Vix</span></li>
    <li><svg width="11" height="11" viewBox="0 0 11 11"><circle cx="5.5" cy="5.5" r="4.6" fill="none" stroke="var(--check)" stroke-width="1.2"/><path d="M3,5.6 L5,7.4 L9.6,2.4" fill="none" stroke="var(--check)" stroke-width="1.4"/></svg>Clarotrack (clear braces)</li>
    <li><svg width="11" height="11" viewBox="0 0 11 11"><circle cx="5.5" cy="5.5" r="4.6" fill="none" stroke="var(--check)" stroke-width="1.2"/><path d="M3,5.6 L5,7.4 L9.6,2.4" fill="none" stroke="var(--check)" stroke-width="1.4"/></svg>Dentures/Partial</li>
    <li><svg width="11" height="11" viewBox="0 0 11 11"><circle cx="5.5" cy="5.5" r="4.6" fill="none" stroke="var(--check)" stroke-width="1.2"/><path d="M3,5.6 L5,7.4 L9.6,2.4" fill="none" stroke="var(--check)" stroke-width="1.4"/></svg>Children's Dentistry</li>
    <li style="min-height:34px"><svg width="11" height="11" viewBox="0 0 11 11"><circle cx="5.5" cy="5.5" r="4.6" fill="none" stroke="var(--check)" stroke-width="1.2"/><path d="M3,5.6 L5,7.4 L9.6,2.4" fill="none" stroke="var(--check)" stroke-width="1.4"/></svg>Sedation Dentistry/Nitrous Gas<br>(for anxiety reduction)</li>
    <li><svg width="11" height="11" viewBox="0 0 11 11"><circle cx="5.5" cy="5.5" r="4.6" fill="none" stroke="var(--check)" stroke-width="1.2"/><path d="M3,5.6 L5,7.4 L9.6,2.4" fill="none" stroke="var(--check)" stroke-width="1.4"/></svg>Emergency Treatment</li>
  </ul>

  <h2 class="section-title section-title--testimonials">TESTIMONIALS</h2>
  <span class="quote-mark quote-mark--open">&ldquo;</span>
  <div class="testimonials">
    <p class="testimonial">By far the best dentists I have been too! Both Dr. Keswicks are an absolute joy to see. The staff treats you like family every time you walk in the door. Marbrook Dentistry makes going to the dentist a pleasure. If you are looking for new dentist or are new to the area.....this is the place you want. A+ all the way.</p>
    <div class="testimonial-divider"></div>
    <p class="testimonial">Marbrook Family Dentistry offers superior care! Both dentists are well-educated, caring, professionals who are looking to build lasting relationships with their patients! They give honest second opinions too! If you haven't received excellent care from a dentist in the past, contact Marbrook Family Dentistry in Larkfield for an appointment!</p>
  </div>
  <span class="quote-mark quote-mark--close">&rdquo;</span>
</section>

</body>
</html>
```